Refresh look of our invoices (Excel spreadsheet which converts to PDF) to better match our new look

We have recently updated our Website and other marketing material with a new look and would like to refresh our invoice template so that it better matches our new look.  The template is an excel spreadsheet which we convert to a PDF to send out to our clients.
The main requirement is to incorporate the newer design colours and general look/feel to align with what is on our website www.corvalhill.com.au
It is extremely important that excel formula functionality and general layout are much the same although we are open to any design suggestions you might have.
Please note:
-Totals figures and news panel must remain on the first page
-We need full ability to edit embedded formulas and Excel spreadsheet is NOT to be password protected as we will only be using it internally.
-It is crucial that the second and subsequent pages can be extended (duplicated) internally to allow for larger multi page entries. Some of our clients invoices run up to 4/5 pages in length and we need the abilty to keep adding rows)
-possibility to add a "convert to PDF" button within the sheet which provides a 1 click solution to convert to PDF rather than the manual 2 step process to convert.... If that can be done, we would not want the "convert to PDF" button to show on final PDF converted version we issue to our customers.   Ideally, a single "convert to PDF and print first cover page only" in 1 single click button named 'convert to PDF & print' would be really handy.  -  (Just to explain why - we email out a PDF version of invoice to our clients and only print off first page with totals for our records)
The design for the first page can be different from the second & subsequent pages (eg first page can be more fancy with following pages more basic)

Finance Industry
Marketing

```html
<!DOCTYPE html>
<html lang="en">
<head>
<meta charset="utf-8">
<title>Corval Hill – Recipient Created Tax Invoice</title>
<link rel="stylesheet" href="https://fonts.googleapis.com/css2?family=Cabin:wght@400;500;700&family=Carlito&display=swap">
<style>
  :root {
    --brand-green: #5aab35;
    --brand-dark: #3f5a3b;
    --panel-light: #e9f2e6;
    --row-a: #d3e3cf;
    --row-b: #e6efe3;
    --rule: #b9cdb4;
    --ink: #1f1f1f;
    --logo-ink: #3b3d3b;
    --white: #ffffff;
  }
  * { box-sizing: border-box; margin: 0; padding: 0; }
  html, body { width: 978px; height: 1200px; overflow: hidden; background: var(--white); }
  body { font-family: "Cabin", "Gill Sans", sans-serif; color: var(--ink); }
  .invoice { position: relative; width: 978px; height: 1200px; }

  .masthead { position: absolute; left: 0; top: 0; width: 978px; height: 149px; background: var(--brand-green);
    display: flex; align-items: center; justify-content: center; }
  .brand-name { font-family: "Cabin", sans-serif; font-weight: 500; font-size: 54px; letter-spacing: 4px; color: var(--logo-ink); }

  .doc-bar { position: absolute; left: 0; top: 149px; width: 978px; height: 48px; background: var(--brand-dark);
    color: var(--white); display: flex; align-items: center; justify-content: space-between; padding: 0 6px; }
  .doc-title { font-size: 18px; letter-spacing: 0.2px; }
  .doc-abn { font-size: 11px; }

  .details { position: absolute; left: 0; top: 197px; width: 978px; height: 261px; background: var(--panel-light); }
  .issuer { position: absolute; left: 6px; top: 42px; font-size: 20px; line-height: 27px; }
  .meta { position: absolute; left: 412px; font-family: "Carlito", "Calibri", sans-serif; font-size: 16.5px; }
  .meta dt, .meta dd { position: absolute; white-space: nowrap; }
  .meta dd { left: 129px; }

  .line-items { position: absolute; left: 0; top: 458px; width: 978px; }
  .row { display: grid; grid-template-columns: 420px 106px 25px 25px 150px 26px 26px 189px 11px;
    height: 31.6px; align-items: center; font-size: 17px; border-bottom: 1px solid var(--rule); }
  .row:nth-child(odd) { background: var(--row-a); }
  .row:nth-child(even) { background: var(--row-b); }
  .row .desc { padding-left: 6px; }
  .row .units { text-align: center; }
  .row .num { text-align: right; }
  .row .cur { text-align: left; }
  .head-row { display: grid; grid-template-columns: 420px 106px 89px 140px 212px 11px; height: 31px; align-items: center;
    background: var(--brand-dark); color: var(--white); font-weight: 700; font-size: 18px; }
  .head-row .desc { padding-left: 6px; }
  .head-row span { text-align: center; }
  .head-row .desc { text-align: left; }
  .items-end { height: 4px; background: #8fa8a4; }

  .summary { position: absolute; left: 0; top: 842px; width: 978px; }
  .sum-row { position: relative; height: 31.5px; font-size: 17px; }
  .sum-row .label { position: absolute; right: 258px; top: 5px; }
  .sum-row .cur { position: absolute; left: 752px; top: 5px; }
  .sum-row .value { position: absolute; right: 11px; top: 5px; }
  .total-row { position: absolute; left: 0; top: 998px; width: 978px; height: 45px; background: var(--row-a); font-weight: 700; font-size: 19px; }
  .total-row .label { position: absolute; right: 258px; top: 11px; letter-spacing: 0.5px; }
  .total-row .cur { position: absolute; left: 752px; top: 11px; }
  .total-row .value { position: absolute; right: 11px; top: 11px; }

  .news { position: absolute; left: 0; top: 1043px; width: 978px; height: 157px; background: var(--brand-green);
    color: var(--white); padding: 17px 6px 0; font-size: 13.6px; line-height: 18px; }
  .news p + p { margin-top: 11px; }
</style>
</head>
<body>
<main class="invoice">
  <header class="masthead">
    <span class="brand-name">CORVAL HILL</span>
  </header>

  <div class="doc-bar">
    <h1 class="doc-title" style="font-weight:400">RECIPIENT CREATED TAX INVOICE</h1>
    <span class="doc-abn">ABN&nbsp; 00 000 000 000</span>
  </div>

  <section class="details">
    <address class="issuer" style="font-style:normal">
      Corval Hill Pty Ltd<br>
      Level 12, 88 Harbour Lane<br>
      Melbourne Vic 3000<br>
      Ph (1300) 555 204<br>
      Fax (1300) 555 208<br>
      www.corvalhill.com.au
    </address>
    <dl class="meta" style="top:0">
      <dt style="top:16px">Invoice No.</dt><dd style="top:16px">[Invoice Number]</dd>
      <dt style="top:46px">Invoice Date:</dt><dd style="top:46px">[Date]</dd>
      <dt style="top:93px">Bill To:</dt><dd style="top:93px">[Contact]</dd>
      <dd style="top:117px">[Company]</dd>
      <dt style="top:141px">Address:</dt><dd style="top:141px">[Customer Address Line 1]</dd>
      <dd style="top:165px">[Customer Address Line 2]</dd>
      <dt style="top:189px">Phone:</dt><dd style="top:189px">[Customer Phone]</dd>
      <dt style="top:213px">E-mail:</dt><dd style="top:213px">[Customer E-Mail]</dd>
      <dt style="top:237px">Fax:</dt><dd style="top:237px">[Customer Fax]</dd>
    </dl>
  </section>

  <section class="line-items">
    <div class="head-row">
      <span class="desc">Description</span><span>Units</span><span></span><span>Cost Per Unit</span><span>Amount</span><span></span>
    </div>
    <div class="rows">
      <div class="row"><span class="desc">Invoice Data 1</span><span class="units">40</span><span></span><span class="cur">$</span><span class="num">100.00</span><span></span><span class="cur">$</span><span class="num">4,000.00</span><span></span></div>
      <div class="row"><span class="desc">Invoice Data 2</span><span class="units">30</span><span></span><span></span><span class="num">75.00</span><span></span><span class="cur">$</span><span class="num">2,250.00</span><span></span></div>
      <div class="row"><span class="desc">Invoice Data 3</span><span class="units">40</span><span></span><span></span><span class="num">50.00</span><span></span><span class="cur">$</span><span class="num">2,000.00</span><span></span></div>
      <div class="row"><span class="desc">Invoice Data 4</span><span class="units">5</span><span></span><span></span><span class="num">100.00</span><span></span><span class="cur">$</span><span class="num">500.00</span><span></span></div>
      <div class="row"><span class="desc">Invoice Data 5</span><span class="units">70</span><span></span><span></span><span class="num">125.00</span><span></span><span class="cur">$</span><span class="num">8,750.00</span><span></span></div>
      <div class="row"><span class="desc">Invoice Data 6</span><span class="units">25</span><span></span><span></span><span class="num">100.00</span><span></span><span class="cur">$</span><span class="num">2,500.00</span><span></span></div>
      <div class="row"><span class="desc">Invoice Data 7</span><span class="units">5</span><span></span><span></span><span class="num">25.00</span><span></span><span class="cur">$</span><span class="num">125.00</span><span></span></div>
      <div class="row"><span class="desc">Invoice Data 8</span><span class="units">80</span><span></span><span></span><span class="num">116.00</span><span></span><span class="cur">$</span><span class="num">9,280.00</span><span></span></div>
      <div class="row"><span class="desc">Invoice Data 9</span><span class="units">65</span><span></span><span></span><span class="num">85.00</span><span></span><span class="cur">$</span><span class="num">5,525.00</span><span></span></div>
      <div class="row"><span class="desc">Invoice Data 10</span><span class="units">44</span><span></span><span></span><span class="num">60.00</span><span></span><span class="cur">$</span><span class="num">2,640.00</span><span></span></div>
      <div class="row"><span class="desc">Invoice Data 11</span><span class="units">39</span><span></span><span></span><span class="num">102.00</span><span></span><span class="cur">$</span><span class="num">3,978.00</span><span></span></div>
    </div>
    <div class="items-end"></div>
  </section>

  <section class="summary">
    <div class="sum-row"><span class="label">Invoice Subtotal</span><span class="cur">$</span><span class="value">41,548.00</span></div>
    <div class="sum-row"><span class="label">Tax Rate</span><span class="value">8.25%</span></div>
    <div class="sum-row"><span class="label">Sales Tax</span><span class="value">3,427.71</span></div>
    <div class="sum-row"><span class="label">Other</span></div>
    <div class="sum-row"><span class="label">Deposit Received</span><span class="value">5,000.00</span></div>
  </section>

  <div class="total-row"><span class="label">TOTAL</span><span class="cur">$</span><span class="value">39,975.71</span></div>

  <footer class="news">
    <p>* CORVAL LINK - Referral management software *<br>
    The Corval Link software provides you with a fully compliant referral process that is supported by the lenders. Apart from making new referrals, you can also read lender updates on deal progress and lodge enquires for outstanding commission payments. You can login by going to the dedicated Corval Link website at: www.corvalmembers.com.au</p>
    <p>This report contains confidential client information. Disclosure of customer information such as loan details and lenders to third parties may be a contravention of the Privacy Act, unless they are authorised to receive such details.</p>
  </footer>
</main>
</body>
</html>
```